Carver Lindqvist Group Business Cards

We have a new logo, and want to design new business cards with it. We are 21 years in business, and want a fresh but professional look, so not a lot of extra stuff on the card. We are a recruiting and staffing firm focused on placing accounting and finance professionals in the Dallas TX area. I've attached our new logo that should be displayed on the cards. Here is what I think we want on the cards:
Ray Pemberly, CPA
Partner and Managing Director
8282 Orchard Vale Rd.
Suite 610
Dallas, TX 75391
O 214-555-0184
M 214-555-0237
ray@carverlindqvist.example
www.carverlindqvist.example

```html
<!DOCTYPE html>
<html lang="en">
<head>
<meta charset="utf-8">
<title>Carver Lindqvist Group – Business Cards</title>
<link href="https://fonts.googleapis.com/css2?family=Montserrat:wght@500;600;700&display=swap" rel="stylesheet">
<style>
  :root {
    --page-bg: #e6e6e6;
    --card-white: #ffffff;
    --band-grey: #f3f3f4;
    --ink-blue: #2b3f94;
    --navy-top: #253a8c;
    --navy-bottom: #2a2f78;
    --wordmark-light: #6a80c8;
  }
  * { margin: 0; padding: 0; box-sizing: border-box; }
  html, body { width: 1200px; height: 1200px; overflow: hidden; }
  body {
    background: var(--page-bg);
    font-family: "Montserrat", Arial, sans-serif;
    color: var(--ink-blue);
    position: relative;
  }
  .card {
    position: absolute;
    left: 212px;
    width: 776px;
    height: 467px;
    box-shadow: 0 18px 30px rgba(0,0,0,0.25);
    overflow: hidden;
  }
  .card-front { top: 86px; background: var(--card-white); }
  .card-back {
    top: 649px;
    background: linear-gradient(160deg, var(--navy-top), var(--navy-bottom));
  }
  .wordmark {
    position: absolute;
    left: 0; right: 0;
    text-align: center;
    font-weight: 700;
    letter-spacing: -0.5px;
    white-space: nowrap;
  }
  .card-front .wordmark { top: 106px; font-size: 40px; color: var(--ink-blue); }
  .card-back .wordmark { top: 208px; font-size: 44px; color: var(--wordmark-light); }
  .holder-name {
    position: absolute; left: 0; right: 0; top: 260px;
    text-align: center; font-size: 31px; font-weight: 600; letter-spacing: 1px;
  }
  .holder-title {
    position: absolute; left: 0; right: 0; top: 296px;
    text-align: center; font-size: 18px; font-weight: 600; letter-spacing: 0.3px;
  }
  .divider {
    position: absolute; left: 49px; right: 49px; top: 325px;
    height: 2px; background: var(--ink-blue);
  }
  .contact-band {
    position: absolute; left: 0; right: 0; top: 395px; height: 56px;
    background: var(--band-grey);
  }
  .contact-list {
    position: absolute; left: 49px; top: 335px; list-style: none;
  }
  .contact-list li {
    display: flex; align-items: center; height: 23.5px;
    font-size: 18.5px; font-weight: 600;
  }
  .contact-list svg { width: 18px; height: 18px; margin-right: 10px; fill: var(--ink-blue); }
  .address {
    position: absolute; right: 49px; top: 335px;
    text-align: right; font-style: normal; font-size: 18.5px; font-weight: 600;
  }
  .address span { display: block; height: 23.5px; line-height: 23.5px; }
</style>
</head>
<body>
  <section class="card card-front">
    <div class="wordmark">Carver Lindqvist Group</div>
    <div class="holder-name">RAY PEMBERLY, CPA</div>
    <div class="holder-title">PARTNER AND MANAGING DIRECTOR</div>
    <div class="divider"></div>
    <div class="contact-band"></div>
    <ul class="contact-list">
      <li><svg viewBox="0 0 24 24"><path d="M6.6 10.8a15.1 15.1 0 0 0 6.6 6.6l2.2-2.2a1 1 0 0 1 1-.25 11.4 11.4 0 0 0 3.6.57 1 1 0 0 1 1 1V20a1 1 0 0 1-1 1A17 17 0 0 1 3 4a1 1 0 0 1 1-1h3.5a1 1 0 0 1 1 1c0 1.25.2 2.45.57 3.57a1 1 0 0 1-.25 1z"/></svg>214-555-0184</li>
      <li><svg viewBox="0 0 24 24"><path d="M13 2l6 3-8 17-6-3zM13.9 4.6L7.6 18l2.6 1.3 6.3-13.4z"/></svg>214-555-0237</li>
      <li><svg viewBox="0 0 24 24"><path d="M2 5h20v14H2zm2 2v.4l8 5.6 8-5.6V7zm0 2.8V17h16V9.8l-8 5.6z"/></svg>ray@carverlindqvist.example</li>
      <li><svg viewBox="0 0 24 24"><path d="M12 2a10 10 0 1 0 0 20 10 10 0 0 0 0-20zm-1 17.9A8 8 0 0 1 4.2 10L9 14.8v1a2 2 0 0 0 2 2zm6.9-2.5A2 2 0 0 0 16 16h-1v-3a1 1 0 0 0-1-1H8v-2h2a1 1 0 0 0 1-1V7h2a2 2 0 0 0 2-2v-.4a8 8 0 0 1 2.9 12.8z"/></svg>www.carverlindqvist.example</li>
    </ul>
    <address class="address">
      <span>8282 Orchard Vale Rd.</span>
      <span>Suite 610</span>
      <span>Dallas, TX 75391</span>
    </address>
  </section>

  <section class="card card-back">
    <div class="wordmark">Carver Lindqvist Group</div>
  </section>
</body>
</html>
```